Business Card Design Project

We have 2 businesses which help each other.

Brightvale Care (providing nurses to hospitals/nursing homes etc)

and

Brightvale HR (providing nurses to our brightvale care business - but also providing workers for farms, restaurants meatworks etc)

We would like 2 separate business cards - but similar design and feel

Target Market(s)

Managers of nursing homes, hospitals, farms, meatworks, restauants

Industry/Entity Type

Business

Requirements
Must have
• both logos
https://www.filestashly.com/s/9k2m7q4tz1xw5np/BrightvaleHR-Logo-Horizontal.ai
https://www.filestashly.com/s/pe58vn2c0rj4kd/73192_518674_92817_sourcefile.ai

You may edit the layout of Brightvale HR logo

Name
position
mobile
Phone
name@brightvalehr.com.au
brigthvalehr.com.au

Name
position
mobile
phone
name@brightvalecare.net.au
brightvalecare.net.au

```html
<!DOCTYPE html>
<html lang="en">
<head>
<meta charset="utf-8">
<title>Brightvale business cards</title>
<link href="https://fonts.googleapis.com/css2?family=Source+Sans+3:wght@400;600;700&display=swap" rel="stylesheet">
<style>
  :root {
    --page: #ffffff;
    --card-edge: #6b6b6b;
    --hr-blue: #004b93;
    --care-blue: #134a8d;
    --logo-blue: #0d4a8f;
    --care-ink: #2e3391;
    --accent-grey: #c9cdd3;
    --care-accent: #5ab7e6;
    --text-light: #ffffff;
  }
  * { margin: 0; padding: 0; box-sizing: border-box; }
  html, body { width: 1002px; height: 1200px; overflow: hidden; background: var(--page); }
  body { position: relative; font-family: "Source Sans 3", sans-serif; }

  .card {
    position: absolute;
    left: 86px;
    width: 833px;
    background: var(--hr-blue);
    border: 2px solid var(--card-edge);
    overflow: hidden;
  }
  .card--hr { top: 81px; height: 476px; }
  .card--care { top: 635px; height: 475px; background: var(--care-blue); }

  .card__header {
    position: absolute; left: 0; top: 0; width: 100%;
    background: var(--page);
  }
  .card--hr .card__header { height: 118px; }
  .card--care .card__header { height: 181px; }

  .header-bump {
    position: absolute; left: 436px; top: 6px;
    width: 134px; height: 134px; border-radius: 50%;
    background: var(--page);
  }

  .brand-name {
    position: absolute;
    font-weight: 700;
    white-space: nowrap;
    line-height: 1;
    letter-spacing: -0.5px;
  }
  .card--hr .brand-name {
    right: 398px; top: 50px;
    font-size: 50px; color: var(--logo-blue);
  }
  .card--care .brand-name {
    left: 0; width: 100%; text-align: center; top: 82px;
    font-size: 62px; color: var(--care-ink);
  }

  .brand-dot { position: absolute; border-radius: 50%; }
  .card--hr .brand-dot {
    left: 451px; top: 21px; width: 104px; height: 104px;
    background: var(--accent-grey);
  }
  .card--care .brand-dot {
    left: 448px; top: 22px; width: 54px; height: 54px;
    background: var(--care-accent);
  }

  .contact {
    position: absolute; left: 57px;
    list-style: none;
    color: var(--text-light);
    font-size: 29.5px;
    line-height: 39.4px;
  }
  .card--hr .contact { top: 187px; }
  .card--care .contact { top: 214px; }
  .contact__name { font-weight: 700; }
</style>
</head>
<body>

  <section class="card card--hr" aria-label="Brightvale HR business card">
    <div class="card__header">
      <div class="header-bump"></div>
      <span class="brand-name">Brightvale HR</span>
      <span class="brand-dot"></span>
    </div>
    <ul class="contact">
      <li class="contact__name">Name:</li>
      <li>Position:</li>
      <li>Mobile:</li>
      <li>Phone:</li>
      <li>name@brightvalehr.com.au</li>
      <li>brightvalehr.com.au</li>
    </ul>
  </section>

  <section class="card card--care" aria-label="Brightvale Care business card">
    <div class="card__header">
      <span class="brand-dot"></span>
      <span class="brand-name">Brightvale Care</span>
    </div>
    <ul class="contact">
      <li class="contact__name">Name:</li>
      <li>Position:</li>
      <li>Mobile:</li>
      <li>Phone:</li>
      <li>name@brightvalecare.net.au</li>
      <li>brightvalecare.net.au</li>
    </ul>
  </section>

</body>
</html>
```